TBranwell executive consulting

We need a basic clean website for executive consulting. Rosalind is the previos CIO for bluecrest airways and currently supports several technology companies with innovation and transformation.

Target Market(s)

C level technology and CIO training

Industry/Entity Type

Technology and travel industry

Coding

Coded - Design and coding required

Number of Pages Required

3 page

Font styles to use
Sans Serif

Colors
0054AA
0677BA
7BADD7
CADEEF
E8F1F8
0094D4
00A9DD
6FCCEA
C7EBF8
E9F6FB

Requirements
Must have
• Home page, about us, services social media links

```html
<!DOCTYPE html>
<html lang="en">
<head>
<meta charset="utf-8">
<title>TBranwell Executive Consulting</title>
<link rel="stylesheet" href="https://fonts.googleapis.com/css2?family=Poppins:wght@400;500;600;700&family=Tinos:wght@400;700&display=swap">
<style>
:root{
  --blue:#00a9dd;
  --blue-deep:#0094d4;
  --navy:#0054aa;
  --ink:#222;
  --text:#333;
  --muted:#555;
  --bar:#3b3b3d;
  --pale:#eef6fb;
  --dark:#1f1f21;
  --white:#fff;
}
*{box-sizing:border-box;margin:0;padding:0}
html,body{width:1200px;height:3617px;overflow:hidden}
body{position:relative;font-family:"Poppins",sans-serif;color:var(--text);background:var(--white)}
.abs{position:absolute}
.serif{font-family:"Tinos",serif}

/* top bar */
.topbar{left:0;top:0;width:1200px;height:53px;background:var(--bar)}
.topbar .ico{width:24px;height:24px;border-radius:5px;background:var(--blue);top:15px;display:flex;align-items:center;justify-content:center}
.topbar .ico.line{background:none;border:2px solid var(--blue)}
.topbar .txt{top:16px;color:#fff;font-size:14px}
/* nav */
.nav{left:0;top:53px;width:1200px;height:96px;background:#fff}
.logo-box{left:77px;top:0;width:264px;height:146px;background:#fff;box-shadow:0 4px 14px rgba(0,0,0,.15);display:flex;align-items:center;justify-content:center;z-index:3}
.brand{font-family:"Poppins",sans-serif;font-weight:600;color:var(--navy);font-size:30px}
.menu a{position:absolute;top:38px;font-size:14px;color:var(--ink);text-decoration:none}
.menu a.active{color:var(--blue);border-bottom:1px solid var(--blue);padding-bottom:2px}
.nav .cta{left:1036px;top:33px;width:108px;height:29px;background:var(--blue);color:#fff;font-size:14px;display:flex;align-items:center;justify-content:center}

/* hero */
.hero{left:0;top:149px;width:1200px;height:626px;background:linear-gradient(90deg,#8a8a8c 0%,#b9b6b2 22%,#dcdcdc 40%,#f2f2f2 60%,#e6e7e8 100%)}
.hero-title{left:470px;top:124px;width:655px;text-align:center;font-size:64px;line-height:73px;color:#111;font-weight:400}
.hero-text{left:540px;top:358px;width:515px;text-align:center;font-size:14px;line-height:24px;color:#222}
.btn{background:var(--blue);color:#fff;display:flex;align-items:center;justify-content:center;border-radius:6px}
.hero .btn{left:696px;top:445px;width:205px;height:46px;font-size:20px}

/* about */
.eyebrow{font-size:16px;color:var(--ink);display:flex;align-items:center;gap:8px;letter-spacing:.2px}
.eyebrow .dash{width:45px;height:2px;background:var(--blue);position:relative}
.eyebrow .dash::before{content:"";position:absolute;width:5px;height:5px;border-radius:50%;background:var(--blue);top:-1.5px}
.eyebrow .dash.r::before{left:0}
.eyebrow .dash.l::before{right:0}
.sec-title{font-family:"Tinos",serif;font-size:42px;color:#111;font-weight:400;line-height:1}
.about-text{left:138px;top:973px;width:432px;font-size:14.5px;line-height:23.2px;text-align:justify;color:#333}
.about-photo{left:705px;top:851px;width:335px;height:408px;background:linear-gradient(100deg,#bdb8b0 0%,#8e8a84 20%,#f0ece6 45%,#2a2a35 70%,#d8d4cc 100%)}

/* services */
.services{left:0;top:1339px;width:1200px;height:1283px;background:var(--pale)}
.card{width:315px;height:315px;border-radius:3px;overflow:hidden}
.card.photo{background:linear-gradient(180deg,#8d9299 0%,#5b5f66 50%,#1c1d20 100%)}
.card .cap{position:absolute;left:0;right:0;bottom:20px;text-align:center;color:#fff;font-weight:600;font-size:17px;line-height:23px;text-transform:uppercase}
.card.info{background:#fff;box-shadow:0 2px 12px rgba(0,0,0,.12);padding:30px 20px 0 26px}
.card.info h3{font-family:"Tinos",serif;font-weight:400;color:var(--blue-deep);font-size:19px;line-height:23px;text-align:center;text-transform:uppercase;margin-left:-12px}
.card.info ul{list-style:none;margin-top:22px}
.card.info li{position:relative;padding-left:18px;font-size:13px;line-height:23px;color:#222}
.card.info li::before{content:"";position:absolute;left:0;top:9px;width:7px;height:7px;background:var(--blue)}

/* testimonials */
.reviews{left:0;top:2622px;width:1200px;height:505px;background:linear-gradient(180deg,#1e1e20 0%,#262628 60%,#1a1a1b 100%)}
.reviews .eyebrow,.reviews .sec-title{color:#fff}
.quote-text{left:270px;top:310px;width:660px;text-align:center;color:#fff;font-size:14px;line-height:22px}
.who{left:0;width:1200px;text-align:center;color:#fff;font-family:"Tinos",serif}

/* footer */
.footer{left:0;top:3127px;width:1200px;height:490px;background:var(--blue);color:#fff}
.footer h4{font-size:20px;font-weight:600;position:absolute}
.footer .rule{position:absolute;height:1px;background:#fff;width:48px}
.footer .links a{position:absolute;left:540px;font-size:16px;color:#fff;text-decoration:none}
.footer .links a::before{content:"";position:absolute;left:-19px;top:8px;width:6px;height:6px;border-radius:50%;background:#fff}
.footer .citem{position:absolute;left:874px;font-size:19px;line-height:22px}
.footer .cico{position:absolute;left:826px;width:36px;height:36px;border-radius:50%;background:#fff;display:flex;align-items:center;justify-content:center}
.soc{width:36px;height:36px;border-radius:50%;background:#fff;position:absolute;top:3360px}
.copy{left:0;top:3572px;width:1200px;text-align:center;color:#fff;font-size:13px}
</style>
</head>
<body>

<header>
  <div class="abs topbar">
    <div class="abs ico" style="left:624px">
      <svg width="14" height="14" viewBox="0 0 24 24"><path fill="#fff" d="M6.6 10.8a15 15 0 0 0 6.6 6.6l2.2-2.2c.3-.3.7-.4 1-.2 1.1.4 2.3.6 3.6.6.6 0 1 .4 1 1V20c0 .6-.4 1-1 1C10.6 21 3 13.4 3 4c0-.6.4-1 1-1h3.5c.6 0 1 .4 1 1 0 1.3.2 2.5.6 3.6.1.3 0 .7-.2 1z"/></svg>
    </div>
    <span class="abs txt" style="left:669px">555-014-2290</span>
    <div class="abs ico" style="left:793px">
      <svg width="14" height="14" viewBox="0 0 24 24"><path fill="#fff" d="M3 5h18v14H3z"/><path fill="none" stroke="#00a9dd" stroke-width="2" d="M3 6l9 7 9-7"/></svg>
    </div>
    <span class="abs txt" style="left:831px">info@Companyname.com</span>
    <div class="abs ico line" style="left:1049px" aria-label="Social profile"></div>
    <div class="abs ico line" style="left:1083px" aria-label="Social profile"></div>
    <div class="abs ico line" style="left:1116px" aria-label="Social profile"></div>
  </div>

  <div class="abs logo-box"><span class="brand">TBranwell</span></div>

  <nav class="abs nav menu">
    <a class="active" style="left:687px">Home</a>
    <a style="left:760px">About</a>
    <a style="left:836px">Service</a>
    <a style="left:918px">Testimonials</a>
    <div class="abs cta">Contact Us</div>
  </nav>
</header>

<section class="abs hero" role="img" aria-label="Portrait of a smiling businesswoman in a checked blazer in a bright office">
  <h1 class="abs hero-title serif">EXPERIENCED AND PROFESSIONAL ADVISORS</h1>
  <p class="abs hero-text">Lorem ipsum dolor sit amet, consectetur adipiscing elit, sed do eiusmod tempor incididunt ut labore et dolore magna aliqua. Quis</p>
  <div class="abs btn">Know More</div>
</section>

<section class="about">
  <div class="abs eyebrow" style="left:140px;top:896px">WHO WE ARE <span class="dash r"></span></div>
  <h2 class="abs sec-title" style="left:138px;top:922px">ABOUT US</h2>
  <p class="abs about-text">Rosalind Branwell is a seasoned leader with a remarkable 40-year career in the travelindustry, including 20 transformative years at Bluecrest Airways. As the Senior Vice President of Technology (CIO), Rosalind spearheaded some of the company’s mostsignificant technological and strategic transformations, helping Bluecrest Airways stay at the forefront of innovation in the competitive travel market.</p>
  <div class="abs btn" style="left:138px;top:1158px;width:148px;height:56px;font-size:14px;border-radius:7px">Read More</div>

  <svg class="abs" style="left:620px;top:790px" width="510" height="530" viewBox="0 0 510 530" aria-hidden="true">
    <g fill="none" stroke="#0094d4" stroke-width="2">
      <polygon points="169,7 346,16 490,132 484,421 336,525 153,521 17,393 21,103" transform="rotate(0)" opacity="0"/>
      <polygon points="168,6 490,135 362,455 41,327"/>
      <polygon points="345,9 482,412 134,528 15,120" />
    </g>
  </svg>
  <div class="abs about-photo" role="img" aria-label="Portrait of a smiling executive woman in a dark suit in a bright lobby"></div>
</section>

<section class="abs services">
  <div class="abs eyebrow" style="left:490px;top:90px"><span class="dash l"></span> WHO WE DO <span class="dash r"></span></div>
  <h2 class="abs sec-title" style="left:0;width:1200px;text-align:center;top:112px">OUR SERVICES</h2>

  <div class="abs card info" style="left:91px;top:209px">
    <h3>Advisory Services for CIOs and IT Executives</h3>
    <ul>
      <li>Strategic guidance tailored to CIOs and senior IT leaders.</li>
      <li>Support with board presentations, executive communication, and influencing stakeholders.</li>
      <li>Guidance on talent development and succession planning within IT teams.</li>
    </ul>
  </div>
  <div class="abs card photo" style="left:442px;top:209px" role="img" aria-label="Silhouette of a traveller working on a laptop at an airport window"><div class="cap">Technology Strategy<br>Development</div></div>
  <div class="abs card photo" style="left:794px;top:209px;background:linear-gradient(180deg,#9aa39c 0%,#6b6f78 50%,#1c1d22 100%)" role="img" aria-label="Two business colleagues reviewing a tablet together"><div class="cap">Digital Transformation<br>Consulting</div></div>

  <div class="abs card photo" style="left:91px;top:561px;background:linear-gradient(180deg,#a7acb2 0%,#6a6c72 50%,#1d1e21 100%)" role="img" aria-label="Colleagues examining a model airplane"><div class="cap">IT-Business Partnership<br>Development</div></div>
  <div class="abs card photo" style="left:442px;top:561px;background:linear-gradient(180deg,#b5b3ae 0%,#6d6b68 50%,#1d1d1f 100%)" role="img" aria-label="Airline staff pointing while talking in a terminal"><div class="cap">Organizational Change<br>Management</div></div>
  <div class="abs card photo" style="left:794px;top:561px;background:linear-gradient(180deg,#8c8478 0%,#6a6258 50%,#1f1d1b 100%)" role="img" aria-label="Two professionals planning at a desk with a globe"><div class="cap">Program and Project<br>Oversight</div></div>

  <div class="abs card photo" style="left:442px;top:907px;background:linear-gradient(180deg,#c5c8c9 0%,#7a7b7d 50%,#1e1e20 100%)" role="img" aria-label="Three professionals walking through a bright terminal"><div class="cap">Advisory Services for CIOs<br>and IT Executives</div></div>
</section>

<section class="abs reviews" role="region" aria-label="Customer reviews">
  <div class="abs eyebrow" style="left:490px;top:76px;color:#fff"><span class="dash l"></span> TESTIMONIALS <span class="dash r"></span></div>
  <h2 class="abs sec-title" style="left:0;width:1200px;text-align:center;top:100px;color:#fff">CUSTOMER REVIEWS</h2>
  <div class="abs serif" style="left:0;width:1200px;text-align:center;top:185px;font-size:150px;line-height:150px;color:var(--blue);font-weight:700">&ldquo;</div>
  <svg class="abs" style="left:190px;top:310px" width="22" height="30" viewBox="0 0 22 30"><path d="M17 3L5 15l12 12" fill="none" stroke="#0677ba" stroke-width="3"/></svg>
  <svg class="abs" style="left:980px;top:310px" width="22" height="30" viewBox="0 0 22 30"><path d="M5 3l12 12L5 27" fill="none" stroke="#00a9dd" stroke-width="3"/></svg>
  <p class="abs quote-text">Rosalind is a decisive and fair leader who exemplifies strength, wisdom, and empathy. She always possesses a clear vision for the future and is willing to make bold decisions which are grounded in data, expertise, and intuition while remaining open to diverse perspectives.</p>
  <div class="abs who" style="top:388px;font-size:17px;font-weight:700">MARTIN HALE</div>
  <div class="abs who" style="top:414px;font-size:14px">CEO NORVANE</div>
</section>

<footer class="abs footer" style="position:absolute">
  <div class="abs brand" style="left:184px;top:145px;color:#fff;font-size:34px">TBranwell</div>
  <h4 style="left:526px;top:100px">LINKS</h4>
  <div class="rule" style="left:526px;top:137px"></div>
  <div class="links">
    <a style="top:171px">About Us</a>
    <a style="top:203px">Our Services</a>
    <a style="top:235px">Testimonials</a>
    <a style="top:268px">Contact Us</a>
  </div>
  <h4 style="left:824px;top:100px">CONTACT US</h4>
  <div class="rule" style="left:824px;top:137px"></div>
  <div class="cico" style="top:181px"><svg width="18" height="20" viewBox="0 0 24 24"><path fill="#00a9dd" d="M12 2a7 7 0 0 0-7 7c0 5 7 13 7 13s7-8 7-13a7 7 0 0 0-7-7zm0 9.5A2.5 2.5 0 1 1 12 6.5a2.5 2.5 0 0 1 0 5z"/></svg></div>
  <div class="citem" style="top:181px">223,Lorem ipsum<br>Lorem ipsum,Lorem ipsum.</div>
  <div class="cico" style="top:235px"><svg width="18" height="18" viewBox="0 0 24 24"><path fill="#00a9dd" d="M6.6 10.8a15 15 0 0 0 6.6 6.6l2.2-2.2c.3-.3.7-.4 1-.2 1.1.4 2.3.6 3.6.6.6 0 1 .4 1 1V20c0 .6-.4 1-1 1C10.6 21 3 13.4 3 4c0-.6.4-1 1-1h3.5c.6 0 1 .4 1 1 0 1.3.2 2.5.6 3.6.1.3 0 .7-.2 1z"/></svg></div>
  <div class="citem" style="top:242px">8888 888 888</div>
  <div class="cico" style="top:287px"><svg width="18" height="16" viewBox="0 0 24 20"><rect x="2" y="3" width="20" height="14" fill="#00a9dd"/><path d="M2 4l10 7 10-7" fill="none" stroke="#fff" stroke-width="2"/></svg></div>
  <div class="citem" style="top:294px">info@companyname.com</div>
  <div class="abs" style="left:80px;top:414px;width:1065px;height:1px;background:#fff"></div>
</footer>
<div class="soc" style="left:197px" aria-label="Social profile"></div>
<div class="soc" style="left:246px" aria-label="Social profile"></div>
<div class="soc" style="left:292px" aria-label="Social profile"></div>
<div class="abs copy">© 2025 Company Name, Inc. All Rights Reserved.</div>

</body>
</html>
```